Wellness, weight management medical practice

We have a logo but want help designing and finalizing the business card. Japanese name. Will eventually be a holistic, full-service weight management and wellness center. Will be a virtual only practice to start.

```html
<!DOCTYPE html>
<html lang="en">
<head>
<meta charset="utf-8">
<title>Mirasei Wellness – Business Card</title>
<link rel="stylesheet" href="https://fonts.googleapis.com/css2?family=Open+Sans:wght@400;600;700&display=swap">
<style>
  :root {
    --canvas: #222222;
    --paper: #ffffff;
    --gold-deep: #b8802a;
    --gold-mid: #dba52c;
    --gold-light: #fbd84a;
    --gold-text: #d99f1f;
    --ink: #111111;
  }
  * { box-sizing: border-box; margin: 0; padding: 0; }
  html, body {
    width: 1200px; height: 780px; overflow: hidden;
    background: var(--canvas);
    font-family: "Open Sans", sans-serif;
  }
  .canvas {
    position: relative; width: 1200px; height: 780px;
    display: flex; align-items: center; justify-content: center; gap: 60px;
  }
  .card {
    position: relative; width: 540px; height: 309px;
    border-radius: 22px; overflow: hidden;
    background: var(--paper);
    box-shadow: 0 18px 40px rgba(0,0,0,.45);
  }
  .card-bg { position: absolute; inset: 0; width: 100%; height: 100%; }
  .brand {
    position: absolute;
    color: var(--gold-text); font-weight: 600; white-space: nowrap;
  }
  .card-front .brand { left: 50%; top: 50%; transform: translate(-50%, -50%); font-size: 30px; }
  .card-back .brand { left: 38px; top: 96px; font-size: 19px; }
  .divider {
    position: absolute; left: 262px; top: 58px; width: 1.5px; height: 170px;
    background: var(--ink);
  }
  .contact { position: absolute; left: 282px; top: 62px; }
  .contact-name { color: var(--gold-text); font-weight: 700; font-size: 30px; line-height: 1.1; }
  .contact-title { color: var(--ink); font-weight: 700; font-size: 16px; margin: 2px 0 10px; }
  .contact-list { list-style: none; }
  .contact-list li {
    display: flex; align-items: center; gap: 8px;
    color: var(--ink); font-size: 15px; line-height: 1.5;
  }
  .contact-icon { width: 13px; height: 13px; flex: none; }
  .address {
    position: absolute; left: 38px; top: 240px;
    color: var(--ink); font-size: 14px; white-space: nowrap;
  }
</style>
</head>
<body>
<main class="canvas">

  <svg width="0" height="0" style="position:absolute">
    <defs>
      <linearGradient id="gold-foil" x1="0" y1="0" x2="1" y2="1">
        <stop offset="0" style="stop-color:var(--gold-deep)"/>
        <stop offset="0.2" style="stop-color:var(--gold-light)"/>
        <stop offset="0.45" style="stop-color:var(--gold-deep)"/>
        <stop offset="0.6" style="stop-color:var(--gold-mid)"/>
        <stop offset="0.8" style="stop-color:var(--gold-light)"/>
        <stop offset="1" style="stop-color:var(--gold-deep)"/>
      </linearGradient>
    </defs>
  </svg>

  <section class="card card-front" aria-label="Card front">
    <svg class="card-bg" viewBox="0 0 540 309" aria-hidden="true">
      <rect width="540" height="309" fill="url(#gold-foil)"/>
      <ellipse cx="270" cy="154" rx="318" ry="168" transform="rotate(-12 270 154)" fill="var(--paper)"/>
    </svg>
    <div class="brand">Mirasei Wellness</div>
  </section>

  <section class="card card-back" aria-label="Card back">
    <svg class="card-bg" viewBox="0 0 540 309" aria-hidden="true">
      <rect width="540" height="309" fill="url(#gold-foil)"/>
      <ellipse cx="270" cy="154" rx="318" ry="168" transform="rotate(-12 270 154)" fill="var(--paper)"/>
    </svg>
    <div class="brand">Mirasei Wellness</div>
    <div class="divider"></div>
    <div class="contact">
      <p class="contact-name">Lena Marvik</p>
      <p class="contact-title">Managing Director</p>
      <ul class="contact-list">
        <li>
          <svg class="contact-icon" viewBox="0 0 16 16" aria-hidden="true"><path d="M4 1.5l2.3 3-1.4 1.6a9 9 0 0 0 5 5l1.6-1.4 3 2.3-1.3 2.5C7.5 14.5 1.5 8.5 1.5 2.8z" fill="var(--gold-text)"/></svg>
          (555) 014-2290
        </li>
        <li>
          <svg class="contact-icon" viewBox="0 0 16 16" aria-hidden="true"><rect x="1" y="3" width="14" height="10" rx="1.5" fill="var(--gold-text)"/><path d="M1.5 4l6.5 5 6.5-5" stroke="var(--paper)" stroke-width="1.3" fill="none"/></svg>
          hello@mirasei.example
        </li>
        <li>
          <svg class="contact-icon" viewBox="0 0 16 16" aria-hidden="true"><circle cx="8" cy="8" r="7" fill="var(--gold-text)"/><path d="M1 8h14M8 1c-3 3.5-3 10.5 0 14M8 1c3 3.5 3 10.5 0 14" stroke="var(--paper)" stroke-width="1" fill="none"/></svg>
          www.mirasei.example
        </li>
      </ul>
    </div>
    <p class="address">418 Lantern Way Suite 300 Ridgefield, TX 75010</p>
  </section>

</main>
</body>
</html>
```